Design a cool print brochure for an NGO / Give your work a global impact!!

Hi,
I provide a full design brief (below, please scroll) and a mood board (attached) to help you visualize inside my head.. ;-)
I am also available to help and have worked many years in advertising; we will understand each other.
Objective:
To design an A4 folded in two presentation brochure for a non-profit consulting agency called Mer-ova.
Mer-ova works in sustainability and international development = working with NGO’s, governments and private sector on global issues such as global warming, education for all etc.
Strategy:
This document is a first step in developing a communication strategy. It will be distributed during a major international event called the Brenvik Outreach Forum.
Objective:
The double objective of the brochure is:
a) to inform the recipient of what Mer-ova is, in the shortest time possible.
b) to showcase relevant projects to demonstrate Mer-ova experience and expertise.
Target:
Main target:
Existing Mer-ova contacts, such as members of development organizations, NGOs, private sector foundations (CSR), regional networks and other development actors.
NB: the main target already has a certain awareness of Mer-ova: we will try to minimize text to maximize visual impact and readability.
Secondary target:
Mer-ova will also distribute the brochure to new prospects of interest during the Brenvik Forum.
Timing:
We will need to finalize the design and have the files by June 1st to allow time for print before the event.
Content:
The document should be concise, highly readable (no clutter) and include:
1. text (that we will provide)
and
2. visual elements such as images, shapes and info-graphics (that is you).
NB: Mer-ova does not have its own image bank; photos will be provided by you.
Format:
A4 folded in half - 4pp A5 - PORTRAIT FORMAT) with an impactful visual in the front, logo, title and headline (please see examples in the mood board attached).
Design elements:
Mer-ova does not have yet a visual identity (please see: http://mer-ova.org) so there is room for creativity and no graphic chart to follow.
The sector of consulting in international development is rather conservative but our intention is to be disruptive and create a “Wow” effect. We count on you for that!
Therefore, the design should be “structured”, “organized”, “uncluttered” but also “modern”, “impactful”, “highly visual” (think infographic or mind map to describe our services and projects).
Please, take the time to see the attached presentation: I give you guidelines and examples of what we want and what we like.
We are looking forward to seeing your work and I am available for comments, questions and support.
Thank you.
RM
Target Market(s)
The full brief is in the project description: please, scroll through it.
The target market is : our existing clients base, working in sustainable development (read: NGO and Concord Assembly people)
Industry/Entity Type
Ngo
Requirements
Must have
- - Design and color elements: please, no black and white. Our company website is in black and white and without graphics; we want the brochure to break away from that and start creating our brand identity; so please, show us colors and desing elements (shapes, backgrounds, etc).
- You have a chance to showcase your talent in terms of visual identity: what lines, forms, layout and colors can you come up with and apply throughout the brochure and serve as the visual identity of Mer-ova?
- The structure of the document should be:
- - Front cover: design elements + impacful photo (see mood board example attached) +our logo + this headline: "Collective action for sustainable development and impact"
- - Inside front: a graphic representation of "Our Services": such as core activity in the center circle and satellite circles for the services we offer.
- - Inside back:
- 1. Icons and text boxes for "Our projects"
- 2. A world map of the countries where we have worked. Full list of countries is here:
- http://mer-ova.org/experience-1
- - Back cover: our contact + logos of partners.
- Our partners are listed here:
- Please use their original logos (ie, in color).
- The design we will select will serve as a basis for a graphic chart...so more work to come...word to the wise ;)
- Please check out our website mer-ova.org to see what we do etc.
Nice to have
- Icons to reflect our services: what icons can you come up with to describe "training services", "building networks" or "program management"?
- I give examples in the mood board.
Should not have
- We are open to creativity and want to generate a "Wow" effect.
- Just note that the sector is rather conservative so flashy colors and cartoon like characters should be avoided. Think "earth, global change, Concord Assembly, climate" without going too green (it's overdone). ;-)
- Make us stand out in the NGO world
- Now you.

```html
<!DOCTYPE html>
<html lang="en">
<head>
<meta charset="utf-8">
<title>Mer-ova brochure</title>
<link href="https://fonts.googleapis.com/css2?family=PT+Sans+Narrow:wght@400;700&family=Roboto+Condensed:wght@400;700&display=swap" rel="stylesheet">
<style>
:root{
  --orange:#f07a2a;
  --orange-soft:#f6a679;
  --orange-mid:#f28a45;
  --slate:#353a44;
  --teal-soft:#7fd0c4;
  --teal:#2fb8a6;
  --ink:#3a3a3a;
  --grey:#7a7a7a;
  --paper:#ffffff;
  --bg:#e6e6e6;
}
*{margin:0;padding:0;box-sizing:border-box}
html,body{width:879px;height:1200px;overflow:hidden;background:var(--bg)}
body{font-family:"PT Sans Narrow",sans-serif;color:var(--ink)}
.canvas{position:relative;width:879px;height:1200px}
.spread{position:absolute;left:87px;width:705px;height:498px;background:var(--paper);overflow:hidden;box-shadow:0 4px 14px rgba(0,0,0,.18)}
.spread--outside{top:60px}
.spread--inside{top:620px}
.fold{position:absolute;left:352px;top:0;width:1px;height:100%;background:rgba(0,0,0,.08)}
.abs{position:absolute}
.brand{position:absolute;display:flex;align-items:center;gap:7px}
.brand__mark{width:9px;height:9px;background:var(--orange)}
.brand__name{font-family:"Roboto Condensed",sans-serif;font-weight:700;font-size:24px;line-height:1;color:var(--slate)}
.brand--light .brand__name{color:#fff}
.dark-band{position:absolute;left:0;top:73px;width:705px;height:293px;background:var(--slate)}
.intro-text{left:13px;top:82px;width:290px;color:#fff;font-size:9px;line-height:11px}
.placeholder-map{left:17px;top:140px;width:282px;height:112px}
.countries{left:13px;top:280px;width:285px;list-style:none;color:#fff;font-size:6.4px;line-height:7.6px}
.countries li{position:relative;padding-left:12px;margin-bottom:4px}
.countries li::before{content:"";position:absolute;left:0;top:1px;width:5px;height:5px;background:var(--orange)}
.countries b{color:var(--orange);font-weight:400}
.contacts{left:13px;top:391px;list-style:none;font-size:12.5px;color:var(--ink)}
.contacts li{display:flex;align-items:center;gap:12px;height:25px}
.contacts svg{width:18px;height:18px}
.bar-orange{position:absolute;left:0;top:473px;width:705px;height:25px;background:var(--orange)}
.headline{left:369px;top:385px;font-family:"Roboto Condensed",sans-serif;font-weight:700;font-size:15.4px;line-height:18.5px;color:var(--slate)}
.section-head{position:absolute;top:0;left:0;width:705px;height:53px;background:var(--orange)}
.section-title{position:absolute;top:19px;font-family:"Roboto Condensed",sans-serif;font-weight:700;font-size:15.5px;color:#fff}
.body-copy{font-size:9.2px;line-height:11.2px;color:var(--grey)}
.body-copy p{margin-bottom:9px}
.body-copy .lead{color:var(--ink)}
.field-copy{left:13px;top:62px;width:326px}
.bullets{display:flex;gap:14px;list-style:none;font-size:7.6px;line-height:9.8px;color:var(--ink)}
.bullets li{position:relative;padding-left:14px;flex:1;text-align:justify}
.bullets li::before{content:"";position:absolute;left:0;top:1px;width:5px;height:5px;background:var(--orange)}
.field-bullets{left:13px;top:222px;width:326px}
.services-intro{left:365px;top:66px;width:330px;color:var(--ink);text-align:justify;font-size:9px}
.service{position:absolute;width:80px;height:55px;border-radius:6px;color:#fff;font-family:"Roboto Condensed",sans-serif;font-size:5.9px;line-height:6.8px;text-align:center;display:flex;flex-direction:column;align-items:center;justify-content:flex-end;padding:0 3px 5px;box-shadow:0 3px 5px rgba(0,0,0,.18)}
.service svg{width:20px;height:20px;margin-bottom:4px}
.service--research{background:var(--orange-soft)}
.service--facilitation{background:var(--orange-mid)}
.service--training{background:var(--orange)}
.service--methods{background:var(--teal-soft)}
.service--evaluation{background:var(--teal)}
.service--coalition{background:var(--slate)}
.hub{position:absolute;left:433px;top:229px;width:172px;height:50px;border-radius:25px;background:var(--slate);box-shadow:0 0 0 6px #fff,0 0 0 8px #cfcfcf;display:flex;align-items:center;justify-content:center}
.hub .brand{position:static}
.bottom-band{position:absolute;left:0;top:399px;width:352px;height:99px;background:var(--slate)}
.rule-orange{position:absolute;left:0;top:396px;width:705px;height:2px;background:var(--orange)}
.services-bullets{left:365px;top:418px;width:330px}
</style>
</head>
<body>
<div class="canvas">

  <section class="spread spread--outside">
    <div class="dark-band"></div>

    <div class="brand" style="left:15px;top:36px">
      <span class="brand__mark"></span><span class="brand__name">Mer-ova</span>
    </div>
    <div class="brand" style="left:370px;top:36px">
      <span class="brand__mark"></span><span class="brand__name">Mer-ova</span>
    </div>

    <p class="abs intro-text">Mer-ova is the result of the collection and examination of all that previous experience. We combine permanently analysis and practice, and incorporate working methods and techniques that encourage active learning and participation.</p>

    <svg class="abs placeholder-map" role="img" aria-label="World map with pins marking regions of work" viewBox="0 0 282 112">
      <rect width="282" height="112" rx="8" fill="#4a505b"/>
      <g fill="var(--orange)">
        <path d="M50 20a5 5 0 0 1 10 0c0 4-5 9-5 9s-5-5-5-9z"/>
        <path d="M142 16a5 5 0 0 1 10 0c0 4-5 9-5 9s-5-5-5-9z"/>
        <path d="M204 16a5 5 0 0 1 10 0c0 4-5 9-5 9s-5-5-5-9z"/>
        <path d="M146 56a5 5 0 0 1 10 0c0 4-5 9-5 9s-5-5-5-9z"/>
      </g>
    </svg>

    <ul class="abs countries">
      <li><b>Europe:</b> EU 28, Norway, Switzerland, Turkey, Montenegro, Ukraine, Serbia, Moldova, Armenia, Georgia and Belarus.</li>
      <li><b>Asia:</b> China, Vietnam, Thailand, Indonesia, Malaysia, Singapore, Bangladesh, Kyrgyzstan, Kazakhstan and Myanmar.</li>
      <li><b>America:</b> US, Canada, Guatemala, El Salvador, Panamá, Costa Rica, Honduras, Colombia, Perú, Bolivia, Brazil, Argentina, Uruguay and Paraguay.</li>
      <li><b>Africa:</b> South Africa, Mozambique, Ethiopia, Kenya, Uganda, Benin, Senegal, Zimbabwe, Ghana, Tunisia, Egypt and Libya.</li>
    </ul>

    <svg class="abs" role="img" aria-label="Photograph looking up through a glass atrium" style="left:303px;top:79px" width="402" height="287">
      <defs><linearGradient id="atrium" x1="0" y1="0" x2="1" y2="1"><stop offset="0" stop-color="#4f7fa6"/><stop offset=".5" stop-color="#b9d3e6"/><stop offset="1" stop-color="#2d4a66"/></linearGradient></defs>
      <polygon points="13,0 402,0 402,287 0,287" fill="url(#atrium)"/>
    </svg>

    <svg class="abs" style="left:0;top:0;pointer-events:none" width="705" height="498">
      <defs><radialGradient id="hall"><stop offset="0" stop-color="#f08a3c"/><stop offset="1" stop-color="#9a4614"/></radialGradient></defs>
      <circle cx="556" cy="357" r="36" fill="var(--orange)"/>
      <g role="img" aria-label="Photograph of people in a study hall, tinted orange">
        <circle cx="644" cy="376" r="80" fill="url(#hall)"/>
      </g>
    </svg>

    <h1 class="abs headline">COLLECTIVE ACTION<br>FOR SUSTAINABLE<br>DEVELOPMENT AND<br>IMPACT</h1>

    <ul class="abs contacts">
      <li><svg viewBox="0 0 20 20"><circle cx="10" cy="10" r="9" fill="none" stroke="var(--orange)" stroke-width="2"/><path d="M7 5l2 3-1.5 1.5a7 7 0 0 0 3 3L12 11l3 2-1 2c-4 0-8-4-8-8z" fill="var(--orange)"/></svg>+34 600 555 017</li>
      <li><svg viewBox="0 0 20 20"><circle cx="10" cy="10" r="9" fill="none" stroke="var(--orange)" stroke-width="2"/><rect x="5" y="6.5" width="10" height="7" fill="var(--orange)"/><path d="M5 6.5l5 4 5-4" fill="none" stroke="#fff" stroke-width="1"/></svg>info@mer-ova.org</li>
      <li><svg viewBox="0 0 20 20"><circle cx="10" cy="10" r="9" fill="none" stroke="var(--orange)" stroke-width="2"/><circle cx="10" cy="10" r="5.5" fill="none" stroke="var(--orange)" stroke-width="1.2"/><path d="M4.5 10h11M10 4.5c-3 3-3 8 0 11M10 4.5c3 3 3 8 0 11" fill="none" stroke="var(--orange)" stroke-width="1"/></svg>www.mer-ova.org</li>
    </ul>

    <div class="bar-orange"></div>
    <div class="fold"></div>
  </section>

  <section class="spread spread--inside">
    <div class="section-head"></div>
    <h2 class="section-title" style="left:13px">OUR FIELD</h2>
    <h2 class="section-title" style="left:365px">MER-OVA SERVICES</h2>

    <div class="abs body-copy field-copy">
      <p class="lead">Is it possible to deliver effective solutions in the 21st Century without well-managed collaborative action?</p>
      <p>Whether you are a business, a public institution, an NGO or a university; to address global challenges or deliver change at the local level, the capacity to collaborate effectively has become one of the critical elements determining failure from success.</p>
      <p>While that is not new, our own experience shows that more often than not cooperation schemes fail to deliver, precisely because the necessary elements of a collaborative logic are not put in place.</p>
      <p>That is why we decided to create Mer-ova: to help our clients integrate the necessary tools, methods and skills to operate effectively in multi-actor complex environments.</p>
    </div>

    <ul class="abs bullets field-bullets">
      <li>In Mer-ova we are convinced that the link between research and practice holds an enormous potential for developing solutions to improve our capacity to achieve collective goals.</li>
      <li>In Mer-ova we believe that theory cannot be separated from practice. The real background of our work is trying to adapt models to a changing reality.</li>
    </ul>

    <div class="rule-orange"></div>
    <div class="bottom-band"></div>

    <svg class="abs" style="left:0;top:300px" width="352" height="198">
      <defs><radialGradient id="meeting"><stop offset="0" stop-color="#e8894a"/><stop offset="1" stop-color="#8f4518"/></radialGradient></defs>
      <circle cx="230" cy="71" r="28" fill="var(--orange)"/>
      <circle cx="115" cy="99" r="100" fill="#fff"/>
      <g role="img" aria-label="Photograph of a team meeting around a table, tinted orange">
        <circle cx="115" cy="99" r="96" fill="url(#meeting)"/>
      </g>
    </svg>

    <div class="brand brand--light" style="left:236px;top:458px">
      <span class="brand__mark"></span><span class="brand__name">Mer-ova</span>
    </div>

    <p class="abs body-copy services-intro">Mer-ova specializes in the analysis of multi-actor cooperation and the facilitation of processes of change. We believe in the need to improve both the understanding and use of collaborative action. For that, we support value-oriented organisations to integrate a better cooperation logic in their daily practice, whether as part of the internal management process or in the context of their relations with other stakeholders.</p>

    <svg class="abs" style="left:0;top:0;pointer-events:none" width="705" height="498">
      <g fill="none" stroke="#c9c9c9" stroke-width="1">
        <path d="M427 188v12h56v14M529 188v26M613 188v12h-56v14"/>
        <path d="M455 290v12h-28v19M529 290v31M601 290v12h12v19"/>
      </g>
      <g fill="var(--orange)"><circle cx="517" cy="214" r="2"/><circle cx="542" cy="214" r="2"/></g>
      <circle cx="529" cy="298" r="2" fill="var(--teal)"/>
      <circle cx="613" cy="318" r="2" fill="var(--slate)"/>
    </svg>

    <div class="service service--research" style="left:387px;top:133px">
      <svg viewBox="0 0 20 20"><circle cx="10" cy="11" r="7" fill="none" stroke="#fff" stroke-width="1.5"/><circle cx="10" cy="11" r="3" fill="none" stroke="#fff" stroke-width="1.5"/><path d="M10 11l7-7" stroke="#fff" stroke-width="1.5"/></svg>
      RESEARCH &amp; ANALYSIS OF COOPERATION SCHEMES</div>
    <div class="service service--facilitation" style="left:489px;top:133px">
      <svg viewBox="0 0 20 20"><rect x="4" y="6" width="6" height="12" fill="#fff"/><rect x="11" y="2" width="6" height="16" fill="#fff"/></svg>
      FACILITATION OF PROCESSES OF CHANGE</div>
    <div class="service service--training" style="left:573px;top:133px">
      <svg viewBox="0 0 20 20"><circle cx="8" cy="12" r="4.5" fill="none" stroke="#fff" stroke-width="2.2" stroke-dasharray="2 1.5"/><circle cx="14" cy="5" r="3" fill="none" stroke="#fff" stroke-width="1.8" stroke-dasharray="1.6 1.2"/></svg>
      TRAINING TO IMPROVE NETWORKED ACTION</div>

    <div class="hub">
      <div class="brand brand--light">
        <span class="brand__mark"></span><span class="brand__name">Mer-ova</span>
      </div>
    </div>

    <div class="service service--methods" style="left:387px;top:321px">
      <svg viewBox="0 0 20 20"><circle cx="10" cy="5" r="3" fill="#fff"/><rect x="4" y="10" width="12" height="7" fill="#fff"/></svg>
      METHODOLOGIES FOR ORGANIZATIONAL CHANGE &amp; CONSENSUS BUILDING</div>
    <div class="service service--evaluation" style="left:489px;top:321px">
      <svg viewBox="0 0 20 20"><rect x="3" y="4" width="14" height="10" fill="none" stroke="#fff" stroke-width="1.5"/><path d="M6 12l3-3 2 2 3-4M7 17h6" stroke="#fff" stroke-width="1.3" fill="none"/></svg>
      EVALUATION OF MULTI-ACTOR PROJECTS &amp; PROGRAMS</div>
    <div class="service service--coalition" style="left:573px;top:321px">
      <svg viewBox="0 0 20 20"><rect x="3" y="12" width="3" height="6" fill="#fff"/><rect x="8" y="9" width="3" height="9" fill="#fff"/><rect x="13" y="5" width="3" height="13" fill="#fff"/></svg>
      COALITION BUILDING TO ACHIEVE COLLECTIVE GOALS</div>

    <ul class="abs bullets services-bullets">
      <li>Our training aims to equip participants with the theoretical and practical tools to approach collaborative schemes in a more effective way. A special focus is placed on comparative analysis, permanent examples and participatory methodologies.</li>
      <li>We are often approached to develop a methodology to support the organization and facilitation of specific meetings or gatherings. Generally, these are meetings where important decisions have to be taken.</li>
    </ul>

    <div class="fold"></div>
  </section>

</div>
</body>
</html>
```